Letterhead and compliment slip

We are a UK-based market research agency. We are looking for a new letterhead design to incorporate our logo, address details and company information. We are looking for a simple design. It should be modern. It needs to have a qualify feel. As we are UK based it needs to be designed for A4 paper size (letterhead).
I'm really looking for something simple in design terms!
Both letterhead and compliment slip need to include:
Our logo
Company address
Telephone number
Email address
Website address
Company registration number
VAT registration number
Grey and green would be a good colour scheme to fit with our logo

```html
<!DOCTYPE html>
<html lang="en">
<head>
<meta charset="utf-8">
<title>Brightlane Insight Stationery</title>
<link href="https://fonts.googleapis.com/css2?family=Lato:ital,wght@0,400;0,700;1,700&display=swap" rel="stylesheet">
<style>
  :root {
    --bg: #f4f3f3;
    --paper: #ffffff;
    --green: #8dc63f;
    --ink: #2e2e2e;
    --body: #8a8a8a;
    --muted: #6f6f6f;
    --envelope: #a7a8aa;
    --envelope-flap: #9fa0a2;
  }
  * { box-sizing: border-box; margin: 0; padding: 0; }
  html, body { width: 1200px; height: 935px; overflow: hidden; }
  body { background: var(--bg); font-family: "Lato", sans-serif; color: var(--ink); position: relative; }

  .sheet { position: absolute; background: var(--paper); box-shadow: 0 1px 3px rgba(0,0,0,.12); }

  .brand-name { font-family: "Lato", sans-serif; font-weight: 700; color: var(--green); letter-spacing: -0.2px; white-space: nowrap; display: flex; align-items: center; gap: 5px; }
  .brand-dot { width: 9px; height: 9px; border-radius: 50%; background: var(--green); flex: none; }

  .rule { position: absolute; width: 1px; background: var(--green); }

  .contact-list { position: absolute; list-style: none; font-size: 6.3px; line-height: 8.6px; color: var(--muted); }
  .contact-list li { display: flex; align-items: center; gap: 4px; }
  .contact-list svg { width: 5px; height: 5px; fill: var(--green); flex: none; }

  /* Letterhead */
  .letterhead { left: 188px; top: 193px; width: 390px; height: 550px; }
  .letterhead .brand-name { position: absolute; left: 27px; top: 31px; font-size: 19px; }
  .letterhead .rule { left: 210px; top: 23px; height: 34px; }
  .letterhead .contact-list { left: 263px; top: 24px; }
  .letter-body { position: absolute; left: 30px; top: 157px; width: 336px; }
  .salutation { font-size: 8.6px; margin-bottom: 17px; }
  .letter-body p.copy { font-size: 7.3px; line-height: 10px; color: var(--body); margin-bottom: 10px; }
  .sign-off { position: absolute; left: 30px; top: 411px; }
  .sign-off .regards { font-size: 8.4px; margin-bottom: 6px; }
  .sign-off .signer { font-size: 8.2px; }
  .sign-off .role { font-size: 6px; color: var(--muted); margin-top: 2px; }
  .address-band { position: absolute; left: 0; right: 0; top: 523px; height: 12px; background: var(--green); color: #fff; font-size: 6.4px; line-height: 12px; text-align: center; }

  /* Compliment slip */
  .compliment-slip { left: 615px; top: 302px; width: 407px; height: 203px; }
  .compliment-title { position: absolute; right: 22px; top: 23px; font-size: 9.6px; font-weight: 700; font-style: italic; color: var(--green); }
  .slip-footer .brand-name { position: absolute; left: 20px; top: 160px; font-size: 16px; }
  .slip-footer .reg { position: absolute; left: 40px; top: 182px; font-size: 5.2px; color: var(--muted); }
  .slip-footer .rule { top: 157px; height: 28px; }
  .slip-footer .rule.first { left: 148px; }
  .slip-footer .rule.second { left: 287px; }
  .slip-footer .contact-list { left: 171px; top: 159px; font-size: 6px; line-height: 8.4px; }
  .slip-address { position: absolute; left: 309px; top: 159px; font-size: 6px; line-height: 8.4px; color: var(--muted); font-style: normal; }

  /* Envelope */
  .envelope { position: absolute; left: 613px; top: 537px; width: 409px; height: 206px; background: var(--envelope); box-shadow: 0 1px 3px rgba(0,0,0,.12); }
  .envelope-flap { position: absolute; left: 0; top: 0; width: 100%; height: 58px; background: var(--envelope-flap); border-radius: 0 0 8px 8px; box-shadow: 0 2px 3px rgba(0,0,0,.12); display: flex; align-items: center; justify-content: center; }
  .envelope-flap .brand-name { color: #f2f2f2; font-size: 13px; }
  .envelope-flap .brand-dot { background: #f2f2f2; }
</style>
</head>
<body>

<svg width="0" height="0" style="position:absolute">
  <symbol id="icon-phone" viewBox="0 0 10 10"><path d="M2 0.5l2 2-1 1.3c.6 1.3 1.6 2.3 2.9 2.9L7.2 5.7l2 2-1 1.6C4.6 9.5.5 5.4.6 1.6z"/></symbol>
  <symbol id="icon-mail" viewBox="0 0 10 10"><path d="M0 2h10v6H0z M0 2l5 3.4L10 2" /></symbol>
  <symbol id="icon-web" viewBox="0 0 10 10"><circle cx="5" cy="5" r="4.6"/></symbol>
</svg>

<section class="sheet letterhead">
  <div class="brand-name"><span class="brand-dot"></span>Brightlane</div>
  <span class="rule"></span>
  <ul class="contact-list">
    <li><svg><use href="#icon-phone"/></svg>+44 (0)1632 960418</li>
    <li><svg><use href="#icon-mail"/></svg>hello@brightlaneinsight.co.uk</li>
    <li><svg><use href="#icon-web"/></svg>www.brightlaneinsight.co.uk</li>
    <li>Reg: 4810273 | Vat: 572163904</li>
  </ul>

  <div class="letter-body">
    <p class="salutation">Dear sir/Madam,</p>
    <p class="copy">Lorem ipsum dolor sit amet, an vel recteque dissentiet, detracto albucius platonem ex vel, eros repudiandae cu. Atqui aliquando nec an, unum graece adolescens vel ad. Id odio scae has, iudico euismod atomorum ius ea, cum ea honestatis quaerendum theophrastus. Mea honestatis quaerendum theophrastus. Mea</p>
    <p class="copy">Lorem ipsum dolor sit amet, an vel recteque dissentiet, detracto albucius platonem ex vel, eros repudiandae cu. Atqui aliquando nec an, unum graece adolescens vel ad. Id odio scae has, iudico euismod atomorum ius ea, cum ea honestatis quaerendum theophrastus. Mea doming repudiandae ex, cu cum civibus assentior posidonium. Quo etiam pertinax ex, te eros repudiandae cu. Atqui aliquando nec an, unum graece adolescens vel ad. Id odio scae honestatis quaerendum theophrastus. Mea</p>
    <p class="copy">Lorem ipsum dolor sit amet, an vel recteque dissentiet, detracto albucius platonem ex vel, eros repudiandae cu. Atqui aliquando nec an, unum graece adolescens vel ad. Id odio scae has, iudico euismod atomorum ius ea, cum ea honestatis quaerendum theophrastus. Mea honestatis quaerendum theophrastus. Mea</p>
    <p class="copy">eros repudiandae cu. Atqui aliquando nec an, unum graece adolescens vel ad. Id odio scae honestatis quaerendum theophrastus. Mea posidonium. Quo etiam pertinax ex, te etiam pertinax ex, te</p>
  </div>

  <div class="sign-off">
    <p class="regards">Kind Regards</p>
    <p class="signer">Daniel Whitford</p>
    <p class="role">CEO / Founder</p>
  </div>

  <footer class="address-band">12 Maple Yard Harrow Lane Wickford Essex SS11 4QT</footer>
</section>

<section class="sheet compliment-slip">
  <p class="compliment-title">With Compliments ...</p>
  <div class="slip-footer">
    <div class="brand-name"><span class="brand-dot"></span>Brightlane</div>
    <p class="reg">Reg: 4810273 | Vat: 572163904</p>
    <span class="rule first"></span>
    <ul class="contact-list">
      <li><svg><use href="#icon-phone"/></svg>+44 (0)1632 960418</li>
      <li><svg><use href="#icon-mail"/></svg>hello@brightlaneinsight.co.uk</li>
      <li><svg><use href="#icon-web"/></svg>www.brightlaneinsight.co.uk</li>
    </ul>
    <span class="rule second"></span>
    <address class="slip-address">12 Maple Yard Harrow Lane<br>Wickford Essex<br>SS11 4QT</address>
  </div>
</section>

<section class="envelope">
  <div class="envelope-flap">
    <div class="brand-name"><span class="brand-dot"></span>Brightlane</div>
  </div>
</section>

</body>
</html>
```